Health & Fitness Retreat Homepage Design

We have an existing website at http://www.BluePineHavens.com.au which we are retaining but wish to have a freshly designed homepage with the existing top navigation bar.
Sample layout is attached, but feel free to use your creativity on layout and colours, always remembering it needs to fit with the wider site design.
Project Delivery:
5 phase slide slow at top of homepage
Full homepage design and associated files
Target Audience:
- Female 80%, Male 20%
- Aged 30 to 50
- Overweight/Obese (so no pictures of thin people)
See attached layout for more information.
Target Market(s)
Target Audience:
- Female 80%, Male 20%
- Aged 30 to 50
Industry/Entity Type
Fitness
Requirements
Must have
- Must have existing top navigation bar as at http://www.BluePineHavens.com.au and fit with existing interior colours, etc.
Should not have
- No pictures of thin people

```html
<!DOCTYPE html>
<html lang="en">
<head>
<meta charset="utf-8">
<title>BluePineHavens – Weight Loss & Fitness Retreat</title>
<link href="https://fonts.googleapis.com/css2?family=Arimo:wght@400;700&display=swap" rel="stylesheet">
<style>
:root{
  --outer:#cfcac1;
  --outer-light:#ebe8e2;
  --page:#f7f6f2;
  --white:#ffffff;
  --ink:#1d1d1d;
  --ink-soft:#333333;
  --pink:#c3135c;
  --berry:#b2405c;
  --orange:#f58a1f;
  --orange-deep:#ee6a10;
  --orange-link:#ea6a0c;
  --yellow:#f7bb14;
  --yellow-deep:#e79a05;
  --green:#6fb52c;
  --green-light:#e4f1cf;
  --green-dark:#1e6612;
  --navy:#2a2a6e;
  --frame:#1e2030;
}
*{box-sizing:border-box;margin:0;padding:0}
html,body{width:1200px;height:1200px;overflow:hidden}
body{
  font-family:"Arimo",Arial,sans-serif;color:var(--ink);
  background:linear-gradient(90deg,var(--outer-light) 0,var(--outer) 7%,var(--outer-light) 12%,var(--outer-light) 88%,var(--outer) 94%,#bdb7ad 100%);
  position:relative;
}
.abs{position:absolute}
.page{left:84px;top:0;width:1054px;height:1200px;background:linear-gradient(90deg,#dcd8cf,var(--page) 6%,var(--page) 94%,#d4cfc5)}

/* header */
.site-header{left:134px;top:0;width:952px;height:150px;background:var(--white);box-shadow:0 6px 10px rgba(0,0,0,.18)}
.header-curl{left:128px;top:132px;width:964px;height:28px}
.brand{left:162px;top:46px}
.brand-name{font-size:22px;font-weight:700;color:var(--ink-soft)}
.nav-col{top:14px;width:160px}
.nav-col h3{font-size:12px;font-weight:700;color:var(--ink);border-bottom:1px solid #bbb;padding-bottom:5px;margin-bottom:7px}
.nav-col li{list-style:none;font-size:11px;font-weight:700;color:var(--ink);line-height:18px;padding-left:14px;position:relative}
.nav-col li::before{content:"";position:absolute;left:2px;top:6px;border-left:5px solid var(--green);border-top:3px solid transparent;border-bottom:3px solid transparent}
.mag-cover{left:938px;top:8px;width:36px;height:62px;background:linear-gradient(160deg,#f3d4c0,#c64a3b 55%,#7a2b26)}
.mag-text{left:982px;top:10px;font-size:12px;font-weight:700;line-height:13px;color:var(--ink)}
.mag-text .free{font-size:16px;color:var(--pink)}
.mag-text .req{display:inline-block;margin-top:2px;background:#2b2b2b;color:var(--white);font-size:9px;padding:2px 4px;border-radius:3px}
.brochure-btn{left:938px;top:79px;width:98px;height:25px;border-radius:3px;background:linear-gradient(#b6b6b6,#7f7f7f);color:var(--white);font-size:11px;font-weight:700;text-align:center;line-height:25px}

/* hero */
.hero-band{left:142px;top:150px;width:944px;height:420px;background:linear-gradient(90deg,var(--green-light),#d6ebb8 60%,#b9dc85 92%,var(--green) 100%)}
.intro-panel{left:150px;top:206px;width:176px;height:250px;background:linear-gradient(var(--green),#5b9f1f);border-radius:4px}
.intro-head{left:150px;top:206px;width:176px;height:56px;background:var(--white);border-bottom:2px solid #cfd8c0;padding:14px 0 0 14px;font-size:15px;font-weight:700;color:var(--pink);line-height:17px}
.intro-lead{left:164px;top:280px;width:150px;font-size:11px;color:var(--white);line-height:13px}
.intro-list{left:158px;top:316px;width:160px;list-style:none}
.intro-list li{font-size:11px;color:var(--white);line-height:13px;padding-left:18px;position:relative;margin-bottom:11px}
.intro-list li::before{content:"";position:absolute;left:3px;top:2px;width:8px;height:8px;background:var(--yellow);transform:rotate(45deg);border:1px solid var(--white)}
.btn-yellow{background:linear-gradient(#fcd34a,var(--yellow-deep));color:var(--white);font-weight:700;text-align:center;border-radius:4px;box-shadow:0 2px 3px rgba(0,0,0,.25)}
.brochure-cta{left:158px;top:419px;width:162px;height:35px;line-height:35px;font-size:12px}
.offer-tab{left:130px;top:462px;width:184px;height:96px;background:linear-gradient(#2f8a1d,var(--green-dark));border-radius:0 26px 0 26px;padding:15px 0 0 22px;color:var(--white);font-size:13px;font-weight:700;line-height:16px}
.offer-tab .link{color:var(--yellow);text-decoration:underline;margin-top:8px;display:block;font-size:13px}

.slide-frame{left:342px;top:214px;width:720px;height:354px;background:var(--frame);border-radius:4px}
.slide-photo{left:350px;top:222px;width:704px;height:322px;background:linear-gradient(90deg,#c9c9cd,#e3e3e6 45%,#d4d4d8 70%,#bdbdc2)}
.slide-strip{left:342px;top:544px;width:724px;height:26px;background:var(--white);border-radius:0 0 6px 6px}
.slide-title{left:590px;top:232px;width:460px;text-align:center;font-size:25px;font-weight:700;color:var(--pink);line-height:29px}
.slide-sub{left:590px;top:290px;width:460px;text-align:center;font-size:11px;font-weight:700;color:var(--ink-soft)}
.slide-cta{left:664px;top:332px;width:210px;height:36px;line-height:36px;font-size:12.5px}
.slide-nav{left:808px;top:542px;width:160px;height:14px}

.rule{left:174px;top:611px;width:880px;height:2px;background:#9a9a9a}

/* offers */
.offer-banner{left:130px;top:650px;width:616px;height:84px;background:linear-gradient(var(--yellow),var(--orange) 55%,var(--orange-deep));box-shadow:0 3px 5px rgba(0,0,0,.25)}
.offer-banner h2{position:absolute;left:38px;top:22px;font-size:21px;font-weight:700;color:var(--white);text-shadow:1px 1px 1px rgba(0,0,0,.4)}
.offer-banner h2 span{color:var(--green-dark);text-shadow:none}
.offer-banner .view{position:absolute;left:466px;top:48px;font-size:15px;font-weight:700;color:var(--green-dark);text-decoration:underline}

.location{top:756px;width:190px}
.location h4{font-size:12.5px;font-weight:700;line-height:15px;height:36px;color:var(--ink)}
.location .photo{height:116px;margin-bottom:20px}
.location p{font-size:12px;line-height:14.6px;text-align:justify;color:var(--ink);height:164px}
.location a{font-size:12px;color:var(--orange-link);text-decoration:underline;line-height:14px;display:block}
.col-divider{top:744px;width:1px;height:408px;background:#9e9e9e}

.home-bar{left:130px;top:1162px;width:616px;height:44px;background:linear-gradient(var(--yellow),var(--orange));padding:12px 0 0 34px;color:var(--white);font-size:11.5px;line-height:14px}
.home-bar b{font-size:14px;text-decoration:underline}

/* program panel */
.program-panel{left:763px;top:654px;width:303px;height:546px;background:var(--berry);border-radius:4px 4px 0 0}
.program-tab{left:760px;top:666px;width:308px;height:50px;background:var(--white);border-radius:3px;padding:12px 0 0 34px;font-size:12px;line-height:15px;color:var(--ink);box-shadow:0 2px 3px rgba(0,0,0,.2)}
.program-link{left:795px;top:726px;font-size:12px;color:var(--white);text-decoration:underline}
.program-video{left:790px;top:754px;width:250px;height:168px;background:linear-gradient(#7ec3d6,#3b8fb0 60%,#2a6f8e);border:2px solid #f1e3e7}
.play{left:896px;top:800px;width:40px;height:44px}
.program-list{left:790px;top:936px;width:250px;list-style:none}
.program-list li{font-size:12px;line-height:14px;color:var(--white);padding-left:22px;position:relative;margin-bottom:12px;text-align:justify}
.program-list li::before{content:"";position:absolute;left:2px;top:3px;width:8px;height:8px;background:var(--yellow);transform:rotate(45deg);border:2px solid var(--white)}
</style>
</head>
<body>
<div class="abs page"></div>

<header>
  <div class="abs site-header"></div>
  <svg class="abs header-curl" viewBox="0 0 964 28" aria-hidden="true">
    <path d="M6 6 Q0 14 8 20 L18 20 L18 6 Z" fill="#2b2b2b"/>
    <path d="M958 6 Q964 14 956 20 L946 20 L946 6 Z" fill="#2b2b2b"/>
    <path d="M8 4 Q120 26 300 10 Q480 -4 660 12 Q840 26 956 4 L956 0 L8 0 Z" fill="#ffffff"/>
    <path d="M8 4 Q120 26 300 10 Q480 -4 660 12 Q840 26 956 4" fill="none" stroke="#c9c9c9" stroke-width="2"/>
  </svg>

  <div class="abs brand"><span class="brand-name">BluePineHavens</span></div>

  <nav>
    <div class="abs nav-col" style="left:404px">
      <h3>THE BEST PROGRAMS</h3>
      <ul><li>Weight Loss Retreat</li><li>Fitness Camps</li><li>Home Retreat</li></ul>
    </div>
    <div class="abs nav-col" style="left:572px">
      <h3>THE BEST LOCATIONS</h3>
      <ul><li>Blue Mountains, NSW</li><li>Central Coast, NSW</li><li>Victoria (Torquay)</li></ul>
    </div>
    <div class="abs nav-col" style="left:740px">
      <h3>ABOUT BLUEPINE</h3>
      <ul><li>Why choose BluePine</li><li>What clients say....</li><li>Contact us</li><li>FREE Brochure</li><li>Special Offers</li></ul>
    </div>
  </nav>

  <div class="abs mag-cover" role="img" aria-label="Magazine cover with a smiling woman"></div>
  <div class="abs mag-text"><span class="free">FREE</span><br>BLUEPINE<br>MAGAZINE<br><span class="req">REQUEST NOW!</span></div>
  <div class="abs brochure-btn">FREE Brochure</div>
</header>

<section class="hero">
  <div class="abs hero-band"></div>
  <div class="abs intro-panel"></div>
  <h2 class="abs intro-head">TRANSFORM YOUR<br>BODY &amp; LIFE</h2>
  <p class="abs intro-lead">at asutralia's No.1 Weight loss &amp; Fitness Retreat</p>
  <ul class="abs intro-list">
    <li>For all shapes,&nbsp; sizes &amp;<br>fitness levels.</li>
    <li>Stuning locations &amp; 1st<br>class facilities</li>
    <li>amazing weight loss<br>results.</li>
  </ul>
  <div class="abs btn-yellow brochure-cta">REQUEST A BROCHURE</div>
  <div class="abs offer-tab">SPECIAL OFFER:<br>2 FOR 1 AT THE<br>BLUE MOUNTAINS.<span class="link">VIEW OFFERS&gt;&gt;</span></div>

  <div class="abs slide-frame"></div>
  <div class="abs slide-photo" role="img" aria-label="Two cheerful women in casual fitness clothes against a light grey studio backdrop"></div>
  <div class="abs slide-strip"></div>
  <h1 class="abs slide-title">Amazin Weight Loss Resulta<br>&amp; Fitness Transformations</h1>
  <p class="abs slide-sub">with Australia's No.1 Weight Loss Camp &amp; Fitness Retreat</p>
  <div class="abs btn-yellow slide-cta">REQUEST MORE INFORMATION</div>
  <svg class="abs slide-nav" viewBox="0 0 160 14" aria-label="Slide navigation">
    <path d="M2 7 L12 1 L12 13 Z" fill="#2a2a6e"/>
    <circle cx="28" cy="7" r="5.5" fill="#d9d9d9" stroke="#aaa"/>
    <circle cx="50" cy="7" r="5.5" fill="#2a2a6e"/>
    <circle cx="72" cy="7" r="5.5" fill="#d9d9d9" stroke="#aaa"/>
    <circle cx="94" cy="7" r="5.5" fill="#d9d9d9" stroke="#aaa"/>
    <circle cx="116" cy="7" r="5.5" fill="#d9d9d9" stroke="#aaa"/>
    <path d="M148 7 L138 1 L138 13 Z" fill="#2a2a6e"/>
  </svg>
</section>

<div class="abs rule"></div>

<section class="offers">
  <div class="abs offer-banner">
    <h2><span>SPECIAL OFFER:</span> 2 for 1 at the Blue Mountains.</h2>
    <span class="view">View offers&gt;&gt;</span>
  </div>

  <article class="abs location" style="left:157px">
    <h4>Blue Mountains Sydney<br>Weight Loss Retreat</h4>
    <div class="photo" role="img" aria-label="Lake surrounded by green bushland" style="background:linear-gradient(#8fb6d4,#6e9d4a 45%,#3f7a2c)"></div>
    <p>Lorem ipsum dolor sit amet, consecteLorem ipsum dolor sit amet, consectetuer adipiscing elit, sed diam nonummy nibh euismod tincidunt ut laoreet dolore magna aliquam erat volutpat. Ut wisi enim ad minim veniam, quis nostrud exerci tation ullamcorper suscipit lobortis nisl ut aliquip ex ea commodo consequat. Duis</p>
    <a style="font-size:10px;line-height:12px">Blue Mountains Sydney<br>Weight Loss Retreat&gt;&gt;</a>
  </article>
  <div class="abs col-divider" style="left:349px"></div>

  <article class="abs location" style="left:356px">
    <h4>Central Coas NSW<br>Weight Loss Retreat</h4>
    <div class="photo" role="img" aria-label="Aerial view of a coastal resort beside the ocean" style="background:linear-gradient(#6d8a7c,#5d7a52 50%,#3e7f9a 75%,#d8e6ea)"></div>
    <p>Lorem ipsum dolor sit amet, consecteLorem ipsum dolor sit amet, consectetuer adipiscing elit, sed diam nonummy nibh euismod tincidunt ut laoreet dolore magna aliquam erat volutpat. Ut wisi enim ad minim veniam, quis nostrud exerci tation ullamcorper suscipit lobortis nisl ut aliquip ex ea commodo consequat. Duis</p>
    <a>Central Coas NSW<br>Weight Loss Retreat</a>
  </article>
  <div class="abs col-divider" style="left:548px"></div>

  <article class="abs location" style="left:556px;width:194px">
    <h4>Victoria Weight Loss<br>Health Retreats</h4>
    <div class="photo" role="img" aria-label="Bright indoor lap pool with large windows" style="background:linear-gradient(#f2f2ef,#d9dcd8 45%,#9fb9c4 80%,#7ba3b4)"></div>
    <p>Lorem ipsum dolor sit amet, consecteLorem ipsum dolor sit amet, consectetuer adipiscing elit, sed diam nonummy nibh euismod tincidunt ut laoreet dolore magna aliquam erat volutpat. Ut wisi enim ad minim veniam, quis nostrud exerci tation ullamcorper suscipit lobortis nisl ut aliquip ex ea commodo consequat. Duis</p>
    <a>Victoria Weight Loss<br>Health Retreats</a>
  </article>

  <div class="abs home-bar">...or let us come to you<br><b>HOME WEIGHT LOSE &amp; FITNESS RETREAT PROGRAM&gt;&gt;</b></div>
</section>

<aside>
  <div class="abs program-panel"></div>
  <p class="abs program-tab">Change your life at Australia's most<br>popular weight loss &amp; fitness retreat</p>
  <span class="abs program-link">&gt;more about the program&lt;</span>
  <div class="abs program-video" role="img" aria-label="Video still of a group of women doing water exercise in a pool"></div>
  <svg class="abs play" viewBox="0 0 40 44" aria-label="Play video"><path d="M4 4 L36 22 L4 40 Z" fill="#2f6fd0" stroke="#ffffff" stroke-width="2"/></svg>
  <ul class="abs program-list">
    <li>Lorem ipsum dolor sit amet, consecteLorem ipsum dolor sit amet,</li>
    <li>consectetuer adipiscing elit, sed diam nonummy nibh euismod tincidunt ut</li>
    <li>laoreet dolore magna aliquam erat volutpat. Ut wisi enim ad minim</li>
    <li>veniam, quis nostrud exerci tation ullamcorper suscipit lobortis nisl ut aliquip</li>
    <li>ex ea commodo consequat. Duis autem vel eum iriure dolor in hendrerit</li>
    <li>in vulputate velit esse molestie consequat</li>
  </ul>
</aside>
</body>
</html>
```